VELDORA WEBSITE

We need a new look for our current website. Veldora Fast Debt Recovery have been in business since 1977. We want our logo to remain the same however our current website is cluttered and we want something fresh, uncluttered, clean-line and easy to use. Our company colours are red, white and black.
We don't want pictures of people across the top of the page instead, we would like messages to appear (scrolling) across the top on a red background with white writing.
All that is required is from the designer to create a new look home page.
Good afternoon designers,
I have attached another page to the Veldora Website profile. Could you please take a look and word towards creating something which incorporates the blue box.
I look forward to receiving your designs.
Thanks
Tomas

```html
<!DOCTYPE html>
<html lang="en">
<head>
<meta charset="utf-8">
<title>Veldora Fast Debt Recovery</title>
<link rel="stylesheet" href="https://fonts.googleapis.com/css2?family=Questrial&family=Montserrat:wght@700&family=Oswald:wght@300&display=swap">
<style>
:root{
  --red-dark:#8e2a1e;
  --red-mid:#c4473a;
  --red-text:#e0453a;
  --card-red:#c4141c;
  --white:#ffffff;
  --nav-bg:#d0d4d6;
  --ink:#111111;
  --quote:#c6f3ec;
  --band:#d8d6d6;
  --body-text:#c9c9c9;
}
*{margin:0;padding:0;box-sizing:border-box}
html,body{width:1200px;height:1007px;overflow:hidden;background:var(--white)}
body{position:relative;font-family:"Questrial",sans-serif;color:var(--ink)}
.header{position:absolute;left:0;top:0;width:1200px;height:138px;background:var(--white)}
.header-band{position:absolute;left:0;top:0}
.brand{position:absolute;left:352px;top:48px;display:flex;align-items:center;gap:10px;font-size:34px;color:var(--red-dark);letter-spacing:2px}
.brand-mark{width:22px;height:22px;background:var(--red-dark)}
.header-contact{position:absolute;left:737px;top:6px;width:258px;color:var(--white)}
.header-contact h2{font-weight:400;font-size:15px;letter-spacing:1px;margin-left:13px;margin-bottom:8px}
.header-contact p{font-size:9.5px;line-height:24px;letter-spacing:.6px;text-align:justify}
.hero{position:absolute;left:0;top:138px;width:1200px;height:358px;
  background:radial-gradient(ellipse 380px 320px at 720px 140px,#9c9c9c 0%,#5c5c5c 50%,#262626 100%)}
.hero::before{content:"";position:absolute;left:0;top:0;width:210px;height:358px;background:linear-gradient(90deg,#1a1a1a,#353535)}
.nav{position:absolute;left:210px;top:0;width:203px;height:358px;background:var(--nav-bg);border-right:1px solid #9ea2a4}
.nav ul{list-style:none;padding-left:3px}
.nav li{height:45px;font-size:18px;letter-spacing:1px;padding-top:8px;border-bottom:1px solid #2b2b2b;margin-right:6px;white-space:nowrap}
.nav li:last-child{border-bottom:none}
.nav-shadow{position:absolute;left:413px;top:0;width:6px;height:358px;background:#6d6d6d}
.quote{position:absolute;left:424px;color:var(--quote);font-size:18px;line-height:24px;letter-spacing:1.5px}
.quote p{margin-left:42px;width:470px;text-align:justify}
.quote .mark{font-family:Georgia,serif;color:var(--white);font-size:64px;line-height:0;position:relative}
.quote .open{position:absolute;left:0;top:30px}
.quote .close{top:30px;margin-left:8px}
.quote-one{top:46px}
.quote-two{top:214px}
.offers{position:absolute;left:0;top:496px;width:1200px;height:150px;background:var(--band)}
.cards{position:absolute;left:210px;top:6px;display:flex;border:2px solid #555}
.card{width:196px;height:136px;background:var(--white);box-shadow:inset 0 0 8px #777;text-align:center;position:relative;overflow:hidden;font-family:"Oswald",sans-serif}
.card + .card{border-left:2px solid #555}
.card-art{position:absolute;left:28px;top:10px;width:64px;height:70px;border-radius:50%;background:radial-gradient(circle,#e9c3c3 0%,#b3101a 100%)}
.card h3,.card p,.card strong{position:absolute;left:0;width:100%;white-space:nowrap;display:block}
.card h3{top:90px;font-weight:300;font-size:11px;color:var(--card-red)}
.card p{top:108px;font-size:7.5px;font-style:italic;color:#555}
.card strong{top:121px;font-weight:300;font-size:10px;color:var(--card-red)}
.content{position:absolute;left:0;top:646px;width:1200px;height:224px;background:linear-gradient(90deg,#3b3b3b,#4a4a4a 50%,#3b3b3b)}
.article{position:absolute;top:12px;width:380px}
.article h2{font-family:"Montserrat",sans-serif;font-size:17px;color:var(--red-text);margin-bottom:12px;text-shadow:0 0 1px #fff}
.article p{font-size:12.2px;line-height:16px;color:var(--body-text);letter-spacing:.6px;text-align:justify}
.article-left{left:211px}
.article-right{left:621px}
.footer{position:absolute;left:0;top:870px;width:1200px;height:137px;background:linear-gradient(180deg,#929292,#7f7f7f)}
.footer-band{position:absolute;left:0;top:0}
.footer-col{position:absolute;top:10px}
.footer-col h3{font-family:"Montserrat",sans-serif;font-size:17px;letter-spacing:1px;color:var(--ink);margin-bottom:6px}
.footer-col ul{list-style:none;margin-left:16px}
.footer-col li{font-size:12.5px;line-height:16px;color:var(--white);letter-spacing:.6px}
.footer-note{position:absolute;top:122px;left:0;width:1200px;text-align:center;font-size:9px;color:#dcdcdc;letter-spacing:.5px}
</style>
</head>
<body>
<header class="header">
  <svg class="header-band" width="1200" height="138" aria-hidden="true">
    <polygon points="623,0 1200,0 1200,138 678,138" fill="var(--red-dark)"/>
    <polygon points="623,0 720,0 678,138 623,0" fill="var(--red-mid)"/>
  </svg>
  <div class="brand"><span class="brand-mark"></span>VELDORA</div>
  <div class="header-contact">
    <h2>Contact us</h2>
    <p>Lorem Ipsum is simply dummy text of the printing and typesetting industry. Lorem Ipsum has been the industry's standard dummy text ever since the 1500s.</p>
  </div>
</header>

<section class="hero">
  <nav class="nav">
    <ul>
      <li>Home</li><li>About us</li><li>Rates</li><li>Products &amp; Solutions</li>
      <li>Media Centre</li><li>Careers</li><li>Contact us</li><li>Client Login</li>
    </ul>
  </nav>
  <div class="nav-shadow"></div>
  <blockquote class="quote quote-one">
    <span class="mark open">&ldquo;</span>
    <p>Lorem Ipsum is simply dummy text of the printing and typesetting industry. Lorem Ipsum has been the industry's standard dummy text ever since the 1500s.<span class="mark close">&rdquo;</span></p>
  </blockquote>
  <blockquote class="quote quote-two">
    <span class="mark open">&ldquo;</span>
    <p>Lorem Ipsum is simply dummy text of the printing and typesetting industry. Lorem Ipsum has been the industry's standard dummy text ever since the 1500s.<span class="mark close">&rdquo;</span></p>
  </blockquote>
</section>

<section class="offers">
  <div class="cards">
    <div class="card"><div class="card-art" role="img" aria-label="Dart hitting a red target"></div><h3>Commission rates from 11%</h3><p>....and that is all you pay because our service is totally</p><strong>NO RECOVERY - NO CHARGE</strong></div>
    <div class="card"><div class="card-art" role="img" aria-label="Dart hitting a red target"></div><h3>Commission rates from 11%</h3><p>....and that is all you pay because our service is totally</p><strong>NO RECOVERY - NO CHARGE</strong></div>
    <div class="card"><div class="card-art" role="img" aria-label="Dart hitting a red target"></div><h3>Commission rates from 11%</h3><p>....and that is all you pay because our service is totally</p><strong>NO RECOVERY - NO CHARGE</strong></div>
    <div class="card"><div class="card-art" role="img" aria-label="Dart hitting a red target"></div><h3>Commission rates from 11%</h3><p>....and that is all you pay because our service is totally</p><strong>NO RECOVERY - NO CHARGE</strong></div>
  </div>
</section>

<section class="content">
  <article class="article article-left">
    <h2>Lorem Ipsum</h2>
    <p>Lorem Ipsum is simply dummy text of the printing and typesetting industry. Lorem Ipsum has been the industry's standard dummy text ever since the 1500s, when an unknown printer took a galley of type and scrambled it to make a type specimen book. It has survived not only five centuries, but also the leap into electronic typesetting, remaining essentially unchanged. It was popularised in the 1960s with the release of Letraset sheets containing Lorem Ipsum passages, and more recently with desktop publishing software like Aldus PageMaker including versions of Lorem Ipsum</p>
  </article>
  <article class="article article-right">
    <h2>Lorem Ipsum</h2>
    <p>Lorem Ipsum is simply dummy text of the printing and typesetting industry. Lorem Ipsum has been the industry's standard dummy text ever since the 1500s, when an unknown printer took a galley of type and scrambled it to make a type specimen book. It has survived not only five centuries, but also the leap into electronic typesetting, remaining essentially unchanged. It was popularised in the 1960s with the release of Letraset sheets containing Lorem Ipsum passages, and more recently with desktop publishing software like Aldus PageMaker including versions of Lorem Ipsum</p>
  </article>
</section>

<footer class="footer">
  <svg class="footer-band" width="300" height="137" aria-hidden="true">
    <polygon points="0,0 166,0 232,137 0,137" fill="var(--red-dark)"/>
    <polygon points="166,0 288,0 212,96" fill="var(--red-mid)"/>
  </svg>
  <div class="footer-col" style="left:210px"><h3>Lorem Ipsum</h3><ul><li>Lorem Ipsum</li><li>Lorem Ipsum</li><li>Lorem Ipsum</li><li>Lorem Ipsum</li></ul></div>
  <div class="footer-col" style="left:418px"><h3>Lorem Ipsum</h3><ul><li>Lorem Ipsum</li><li>Lorem Ipsum</li><li>Lorem Ipsum</li><li>Lorem Ipsum</li></ul></div>
  <div class="footer-col" style="left:650px"><h3>Lorem Ipsum</h3><ul><li>Lorem Ipsum</li><li>Lorem Ipsum</li><li>Lorem Ipsum</li><li>Lorem Ipsum</li></ul></div>
  <div class="footer-col" style="left:869px"><h3>Lorem Ipsum</h3><ul style="margin-left:24px"><li>Lorem Ipsum</li><li>Lorem Ipsum</li><li>Lorem Ipsum</li><li>Lorem Ipsum</li></ul></div>
  <p class="footer-note">Lorem Ipsum is simply dummy text of the printing and typesetting industry.</p>
</footer>
</body>
</html>
```